Stridewell Outfitters Stationary

At Stridewell Outfit, we know that rehab technology is much more than a tool or machine. It’s mobility for your body and productivity and freedom for your lifestyle to reclaim your life. That’s why we specialize in custom power and manual wheelchairs, scooters, complex seating and positioning, standers, and bathroom equipment that all help you reclaim your life.

Our rehab equipment includes custom power wheelchairs offering complex, customized seating and positioning systems with an array of specialized electronic control features. With a certified staff of Assistive Technology Professionals (ATPs) and technical repair department, we provide knowledgeable assistance to make sure you get the right products needed to reclaim your life – delivered on time, right to your door.

```html
<!DOCTYPE html>
<html lang="en">
<head>
<meta charset="utf-8">
<title>Stridewell Outfitters Stationery</title>
<link rel="stylesheet" href="https://fonts.googleapis.com/css2?family=Questrial&family=Montserrat:wght@500;700&display=swap">
<style>
  :root {
    --navy: #13254a;
    --green: #8cc63f;
    --paper: #ffffff;
    --paper-shade: #f3f4f5;
    --ink: #3a3d42;
    --muted: #6b6f75;
    --backdrop: #e4e6e8;
    --logo-light: #d9dde3;
  }
  * { box-sizing: border-box; margin: 0; padding: 0; }
  html, body { width: 1200px; height: 1000px; overflow: hidden; }
  body {
    background: var(--backdrop);
    font-family: "Montserrat", sans-serif;
    position: relative;
  }
  .card {
    position: absolute;
    left: 250px;
    width: 700px;
    height: 400px;
    border-radius: 4px;
    overflow: hidden;
    box-shadow: 0 12px 30px rgba(0,0,0,0.12);
  }
  .card--back { top: 70px; background: var(--navy); }
  .card--front { top: 530px; background: var(--paper); }

  /* back side */
  .back-logo {
    position: absolute; inset: 0;
    display: flex; flex-direction: column;
    align-items: center; justify-content: center; gap: 10px;
  }
  .back-logo__mark { width: 26px; height: 26px; border-radius: 50%; background: var(--green); }
  .back-logo__name {
    font-family: "Questrial", sans-serif;
    font-size: 60px; color: var(--logo-light); line-height: 1;
  }
  .back-logo__sub {
    font-family: "Questrial", sans-serif;
    font-size: 22px; letter-spacing: 9px; color: var(--logo-light);
  }

  /* front side */
  .front-shade {
    position: absolute; left: 0; top: 0; width: 390px; height: 100%;
    background: linear-gradient(90deg, var(--paper) 60%, var(--paper-shade));
    clip-path: polygon(0 0, 100% 0, 92% 100%, 0 100%);
  }
  .front-brand {
    position: absolute; left: 62px; top: 96px;
  }
  .brand-row { display: flex; align-items: center; gap: 12px; }
  .brand-mark { width: 18px; height: 18px; border-radius: 50%; background: var(--green); }
  .brand-name {
    font-family: "Questrial", sans-serif;
    color: var(--navy); font-size: 46px; line-height: 1;
  }
  .brand-sub {
    font-family: "Questrial", sans-serif;
    color: var(--navy); font-size: 17px; letter-spacing: 7px;
    margin-top: 8px; margin-left: 30px;
  }
  .address {
    margin-top: 22px; margin-left: 30px;
    font-size: 15px; line-height: 1.5; color: var(--ink); font-weight: 500;
  }
  .contact {
    position: absolute; left: 418px; top: 150px;
  }
  .contact__name {
    font-weight: 700; color: var(--green); font-size: 20px; letter-spacing: 0.5px;
  }
  .contact__title { font-size: 14px; color: var(--muted); margin-top: 3px; font-weight: 500; }
  .contact__list { list-style: none; margin-top: 16px; }
  .contact__item {
    display: flex; align-items: center; gap: 10px;
    font-size: 14px; color: var(--ink); font-weight: 500; line-height: 1.6;
  }
  .contact__icon {
    width: 15px; height: 15px; border-radius: 3px; background: var(--green);
    display: flex; align-items: center; justify-content: center;
  }
  .front-bands { position: absolute; left: 0; bottom: 0; }
</style>
</head>
<body>
  <section class="card card--back" aria-label="Business card back">
    <div class="back-logo">
      <div class="back-logo__mark"></div>
      <div class="back-logo__name">Stridewell</div>
      <div class="back-logo__sub">OUTFITTERS</div>
    </div>
  </section>

  <section class="card card--front" aria-label="Business card front">
    <div class="front-shade"></div>
    <div class="front-brand">
      <div class="brand-row">
        <span class="brand-name">Stridewell</span>
        <span class="brand-mark"></span>
      </div>
      <div class="brand-sub">OUTFITTERS</div>
      <p class="address">48 Harbor Crest Drive #210<br>Maple Grove IL 60412</p>
    </div>

    <div class="contact">
      <div class="contact__name">NORA WHITFIELD</div>
      <div class="contact__title">Managing Director</div>
      <ul class="contact__list">
        <li class="contact__item">
          <span class="contact__icon"><svg width="9" height="9" viewBox="0 0 10 10"><path d="M2 1h2l1 2.5-1.2.8a5 5 0 0 0 2 2l.8-1.2L9 6v2c0 .6-.4 1-1 1A8 8 0 0 1 1 2c0-.6.4-1 1-1z" fill="#fff"/></svg></span>
          +61 847-555-0182
        </li>
        <li class="contact__item">
          <span class="contact__icon"><svg width="9" height="9" viewBox="0 0 10 10"><rect x="0.5" y="2" width="9" height="6" fill="none" stroke="#fff"/><path d="M0.5 2l4.5 3.5L9.5 2" fill="none" stroke="#fff"/></svg></span>
          hello@stridewell.com
        </li>
        <li class="contact__item">
          <span class="contact__icon"><svg width="9" height="9" viewBox="0 0 10 10"><circle cx="5" cy="5" r="4.2" fill="none" stroke="#fff"/><path d="M1 5h8M5 1c-2 2.5-2 5.5 0 8M5 1c2 2.5 2 5.5 0 8" fill="none" stroke="#fff" stroke-width="0.8"/></svg></span>
          www.stridewell.com
        </li>
      </ul>
    </div>

    <svg class="front-bands" width="700" height="40" viewBox="0 0 700 40" aria-hidden="true">
      <rect x="0" y="26" width="370" height="14" fill="var(--navy)"/>
      <polygon points="352,12 700,12 700,40 376,40" fill="var(--green)"/>
    </svg>
  </section>
</body>
</html>
```